Popup Nightclub Grand Opening Flyer

We need to design a flyer for the grand opening of an upscale, exclusive nightclub called "Lanternfall". The design needs to be chic and exclusive. The background should be black and the text should primarily be white. We like minimalist designs.

Here is the text for the flyer
-
Velvetrope Atlanta Presents

Lanternfall (LOGO)

A Popup Nightclub Experience
For one night Only

Friday, October 18, 2013
Party begins at 9PM

INVITE ONLY

See invitation for location details
(Velvetrope Atlanta logo)

-
Examples we like

http://cdn2-b.brivelpost.com/sites/default/files/styles/image_content_width/hash/3d/fa/1472093815_4471_flyer.jpg?itok=R8kqWm2z

http://api.plovra.com/files/7Kqq-Tr82XXB3pQzJvmtR5HL2W719E4nbRtC6KLd4HsfM8Y2qTDK-VmjwDoNqLX4QBzTHD9nakRbVx3m-Pfq8htc3MDTWr5p4/2zelSaturdays.jpg

http://quenmar.com/wp-content/uploads/yootheme/widgetkit/gallery/2zel/2zel-gen_vroom4-01.jpg

Hi All, one thing that we are seeing that we don't like is on over emphasis on the phrase "a popup nightclub experience" please don't make this the largest thing on the flyer

Target Market(s)

Target market is 25-35 year olds who are affluent (rich) and like luxury brands

Requirements
Must have
• Dark Background
Nice to have
• Velvetrope Logo on the bottom
Modern text that isn't curvy
Should not have
• Curved text

```html
<!DOCTYPE html>
<html lang="en">
<head>
<meta charset="utf-8">
<title>Velvetrope Atlanta presents Lanternfall Nightclub</title>
<link rel="stylesheet" href="https://fonts.googleapis.com/css2?family=Michroma&family=Syncopate:wght@400;700&display=swap">
<style>
  :root {
    --page: #ffffff;
    --panel-dark: #0b0b0c;
    --panel-mid: #2b2b2d;
    --edge: #5a2fa8;
    --edge-top: #8a8a90;
    --text: #f2f2f2;
    --text-soft: #c9c9cc;
    --steel-light: #e9e9ea;
    --steel-dark: #8d8d92;
    --band-text: #1a1a1a;
  }
  * { margin: 0; padding: 0; box-sizing: border-box; }
  html, body { width: 946px; height: 1200px; overflow: hidden; background: var(--page); }
  .flyer {
    position: relative;
    width: 946px;
    height: 1200px;
    background: var(--page);
    font-family: "Michroma", "Arial", sans-serif;
    color: var(--text);
  }
  .panel {
    position: absolute;
    left: 54px; top: 44px;
    width: 840px; height: 1092px;
    border-left: 3px solid var(--edge);
    border-bottom: 3px solid var(--edge);
    border-right: 1px solid var(--edge);
    border-top: 1px solid var(--edge-top);
    background:
      radial-gradient(ellipse 70% 45% at 50% 42%, var(--panel-mid) 0%, rgba(20,20,22,0.6) 55%, transparent 100%),
      repeating-linear-gradient(180deg, rgba(255,255,255,0.035) 0 2px, transparent 2px 7px),
      var(--panel-dark);
    overflow: hidden;
  }
  .line {
    position: absolute;
    left: 0; width: 100%;
    text-align: center;
    text-transform: uppercase;
    white-space: nowrap;
    line-height: 1;
  }
  .presenter { font-size: 31px; letter-spacing: 1px; }
  .presenter-1 { top: 96px; }
  .presenter-2 { top: 136px; }
  .presenter-3 { top: 175px; }
  .brand-mark {
    position: absolute;
    left: 380px; top: 272px;
    width: 80px; height: 80px;
    border-radius: 50%;
    background: var(--steel-light);
  }
  .brand-name { top: 420px; font-size: 52px; letter-spacing: 8px; }
  .brand-sub { top: 484px; font-size: 24px; letter-spacing: 9px; }
  .headline { font-size: 44px; letter-spacing: 0; }
  .headline-1 { top: 532px; }
  .headline-2 { top: 582px; font-family: "Syncopate", "Arial", sans-serif; font-weight: 700; color: var(--steel-light); font-size: 42px; }
  .headline-3 { top: 630px; font-family: "Syncopate", "Arial", sans-serif; font-weight: 700; font-size: 42px;
    background: linear-gradient(180deg, var(--steel-light) 0%, var(--steel-dark) 100%);
    -webkit-background-clip: text; background-clip: text; color: transparent; }
  .headline-4 { top: 680px; }
  .headline-5 { top: 728px; }
  .dot {
    position: absolute;
    left: 418px;
    width: 5px; height: 5px;
    background: var(--text);
  }
  .dot-top { top: 772px; }
  .dot-bottom { top: 908px; }
  .event-date { top: 812px; font-size: 17px; text-transform: none; letter-spacing: 0.5px; }
  .event-time { top: 834px; font-size: 17px; text-transform: none; letter-spacing: 0.5px; }
  .access { top: 866px; font-size: 34px; color: var(--text-soft); letter-spacing: 1px; }
  .info-band {
    position: absolute;
    left: 0; top: 952px;
    width: 100%; height: 26px;
    background: linear-gradient(90deg, var(--steel-dark) 0%, var(--steel-light) 45%, var(--steel-light) 60%, var(--steel-dark) 100%);
    color: var(--band-text);
    font-size: 14px;
    line-height: 26px;
    text-align: center;
    white-space: nowrap;
  }
</style>
</head>
<body>
  <div class="flyer">
    <section class="panel">
      <p class="line presenter presenter-1">Velvetrope</p>
      <p class="line presenter presenter-2">Atlanta</p>
      <p class="line presenter presenter-3">Presents</p>

      <div class="brand-mark"></div>
      <h1 class="line brand-name">Lanternfall</h1>
      <p class="line brand-sub">Nightclub</p>

      <h2 class="line headline headline-1">A Popup</h2>
      <p class="line headline headline-2">Nightclub</p>
      <p class="line headline headline-3">Experience</p>
      <p class="line headline headline-4">For One</p>
      <p class="line headline headline-5">Night Only</p>

      <span class="dot dot-top"></span>
      <p class="line event-date">Friday, October 18, 2013</p>
      <p class="line event-time">Party begins at 9PM</p>
      <p class="line access">Invite Only</p>
      <span class="dot dot-bottom"></span>

      <p class="info-band">address: xxxxxxxxxxxxxxxx xxxxxxxx Ph: 0000 0000 0000 W: samplesite.com</p>
    </section>
  </div>
</body>
</html>
```